Commercial painting company is looking for a creative website designer.

Hi, we just completed our logo project and now ready to launch our website. The project will be done on Squarespace platform. It will contain:
Page 1 HOME
Page 2 SERVICES
Page 3 PICTURES
The content will be written by us. I am not sure bout the pictures, I do not have any to provide. I can buy stock photos if needed.
We are commercial only painting company and have to appeal to commercial, industrial property mangers. We will need CALL, REQUEST FOR ESTIMATE buttons.
If possible to have a live picture on home page would be great. Thank you
Target Market(s)
Property Managers
Industry/Entity Type
Commercial Painting
Other font styles liked:
- Poppins

```html
<!DOCTYPE html>
<html lang="en">
<head>
<meta charset="utf-8">
<title>Summit Coat Works – Commercial &amp; Industrial Painting</title>
<link href="https://fonts.googleapis.com/css2?family=Poppins:wght@300;400;500;600;700&family=Oswald:wght@400&display=swap" rel="stylesheet">
<style>
:root{
  --navy:#0c2a6b;
  --red:#c20a2e;
  --grey:#ececec;
  --white:#ffffff;
  --text:#555a66;
}
*{box-sizing:border-box;margin:0;padding:0}
html,body{width:1200px;height:2913px;overflow:hidden}
body{position:relative;background:var(--white);font-family:'Poppins',sans-serif;color:var(--navy)}
.abs{position:absolute}
.phone-num{font-family:'Oswald',sans-serif;font-weight:400}
.btn{position:absolute;display:flex;align-items:center;justify-content:center;gap:8px;border-radius:20px;font-size:10px;font-weight:600;text-transform:uppercase;letter-spacing:.2px}
.btn-red{background:var(--red);color:var(--white)}
.btn-outline{border:2px solid var(--navy);color:var(--navy);background:transparent}
.photo{position:absolute}
/* header */
.site-header{position:absolute;left:0;top:0;width:1200px;height:75px;background:var(--white);z-index:3}
.brand{position:absolute;left:200px;top:8px;width:134px;height:124px;background:var(--white);border-radius:0 0 67px 67px;display:flex;flex-direction:column;align-items:center;justify-content:center;gap:6px;z-index:4}
.brand-dot{width:38px;height:38px;border-radius:50%;background:var(--navy)}
.brand-name{font-size:13px;font-weight:700;color:var(--navy);text-align:center;line-height:1.2}
.nav a{position:absolute;top:30px;font-size:11px;color:var(--navy);text-decoration:none}
.nav a.active{color:var(--red)}
.header-phone{position:absolute;left:728px;top:26px;font-size:16px;color:var(--navy);display:flex;gap:8px;align-items:center}
/* hero */
.hero{position:absolute;left:0;top:75px;width:1200px;height:450px;background:linear-gradient(160deg,#4b5f86 0%,#8a93a5 40%,#b9bcc3 70%,#9aa0ab 100%)}
.hero-shade{position:absolute;inset:0;background:rgba(40,50,75,.35)}
.hero-title{position:absolute;left:200px;top:131px;color:var(--white);font-size:30px;line-height:45px;text-transform:uppercase;font-weight:300}
.hero-title b{font-weight:700}
.quote{position:absolute;left:731px;top:131px;width:269px;height:413px;background:var(--navy);z-index:2;color:var(--white)}
.quote h2{position:absolute;top:28px;width:100%;text-align:center;font-size:19px;font-weight:700}
.quote p{position:absolute;top:58px;width:100%;text-align:center;font-size:11px}
.field{position:absolute;left:26px;width:218px;height:31px;background:var(--white);border-radius:3px;font-size:9px;color:#333;padding:10px 14px}
/* about */
.about{position:absolute;left:0;top:520px;width:1200px;height:526px;background:var(--grey)}
.big-mark{position:absolute;left:200px;top:594px;width:388px;height:388px;border-radius:50%;border:10px solid var(--navy);display:flex;align-items:center;justify-content:center}
.big-mark span{font-size:34px;font-weight:700;color:var(--navy);text-align:center;line-height:1.25}
.eyebrow{position:absolute;left:613px;top:642px;font-size:12px;font-weight:600}
.eyebrow em{font-style:normal;color:var(--red)}
.about-title{position:absolute;left:613px;top:670px;font-size:25px;line-height:30px;font-weight:400;text-transform:uppercase;width:400px;color:var(--navy)}
.about-title b{font-weight:600}
.about-copy{position:absolute;left:613px;top:780px;width:385px;font-size:10px;line-height:19px;color:var(--text)}
.rule{position:absolute;left:200px;top:1045px;width:800px;height:1px;background:var(--red)}
/* sections */
.section-title{position:absolute;left:0;width:1200px;text-align:center;font-size:25px;font-weight:400;text-transform:uppercase}
.section-title b{font-weight:600}
.card h3{position:absolute;font-size:12px;font-weight:600;text-transform:uppercase}
.card p{position:absolute;width:230px;font-size:10px;line-height:15px;color:var(--text)}
/* cta */
.cta{position:absolute;left:0;top:1816px;width:1200px;height:200px;background:var(--red)}
.cta h2{position:absolute;left:200px;top:64px;color:var(--white);font-size:25px;line-height:30px;font-weight:400;text-transform:uppercase}
.cta h2 b{font-weight:700}
.cta-phone{position:absolute;left:856px;top:67px;width:144px;height:36px;border-radius:18px;background:var(--white);color:var(--navy);display:flex;align-items:center;justify-content:center;gap:8px;font-size:15px}
/* footer */
.site-footer{position:absolute;left:0;top:2590px;width:1200px;height:323px;background:var(--grey)}
.foot-brand{position:absolute;left:200px;top:57px;width:150px;height:150px;border-radius:50%;border:6px solid var(--navy);display:flex;align-items:center;justify-content:center;text-align:center;font-size:15px;font-weight:700;line-height:1.25;color:var(--navy)}
.site-footer h4{position:absolute;top:57px;font-size:14px;font-weight:600}
.foot-list{position:absolute;top:97px;list-style:none;font-size:10px;line-height:22.6px}
.contact-line{position:absolute;left:431px;display:flex;gap:10px;font-size:11px;line-height:15px;align-items:flex-start}
.social{position:absolute;top:208px;width:30px;height:30px;border-radius:50%;background:var(--navy)}
.copyright{position:absolute;left:200px;top:270px;font-size:10px}
.copyright em{font-style:normal;color:var(--red);font-weight:500}
</style>
</head>
<body>

<header class="site-header">
  <div class="brand"><div class="brand-dot"></div><div class="brand-name">Summit<br>Coat Works</div></div>
  <nav class="nav">
    <a class="active" style="left:435px">Home</a>
    <a style="left:497px">Services</a>
    <a style="left:572px">Gallery</a>
    <a style="left:641px">Contact Us</a>
  </nav>
  <div class="header-phone phone-num">
    <svg width="13" height="13" viewBox="0 0 24 24"><path fill="#c20a2e" d="M6.6 10.8a15 15 0 0 0 6.6 6.6l2.2-2.2a1 1 0 0 1 1-.25 11.4 11.4 0 0 0 3.6.57 1 1 0 0 1 1 1V20a1 1 0 0 1-1 1A17 17 0 0 1 3 4a1 1 0 0 1 1-1h3.5a1 1 0 0 1 1 1c0 1.25.2 2.45.57 3.57a1 1 0 0 1-.25 1z"/></svg>
    123-456-7890
  </div>
  <div class="btn btn-red" style="left:856px;top:19px;width:144px;height:36px;font-size:9.5px">Request for Estimate</div>
</header>

<section class="hero">
  <div class="photo" role="img" aria-label="Photo of a large modern commercial building under a blue sky" style="inset:0"></div>
  <div class="hero-shade"></div>
  <h1 class="hero-title">Commercial &amp; Industrial<br><b>High Quality Painting<br>Services</b></h1>
  <div class="btn" style="left:200px;top:292px;width:124px;height:36px;background:var(--navy);color:#fff;font-family:'Oswald',sans-serif;font-size:14px;font-weight:400">
    <svg width="12" height="12" viewBox="0 0 24 24"><path fill="#fff" d="M6.6 10.8a15 15 0 0 0 6.6 6.6l2.2-2.2a1 1 0 0 1 1-.25 11.4 11.4 0 0 0 3.6.57 1 1 0 0 1 1 1V20a1 1 0 0 1-1 1A17 17 0 0 1 3 4a1 1 0 0 1 1-1h3.5a1 1 0 0 1 1 1c0 1.25.2 2.45.57 3.57a1 1 0 0 1-.25 1z"/></svg>123-456-7890</div>
  <div class="btn btn-red" style="left:337px;top:292px;width:113px;height:36px">Contact Us</div>
  <svg class="abs" style="left:0;bottom:0" width="1200" height="80" viewBox="0 0 1200 80" preserveAspectRatio="none">
    <path fill="#ececec" d="M0 62 C80 55 140 70 210 58 C300 42 380 56 460 45 C560 30 640 40 720 28 C820 12 900 30 980 22 C1060 16 1120 26 1200 20 L1200 80 L0 80Z"/>
  </svg>
</section>

<form class="quote">
  <h2>GET FREE QUOTE</h2>
  <p>Instantly Book Your Service Today!</p>
  <div class="field" style="top:94px">Your Name</div>
  <div class="field" style="top:138px">Email</div>
  <div class="field" style="top:182px">City</div>
  <div class="field" style="top:226px">Services</div>
  <div class="field" style="top:269px;height:62px">Type your Message ..</div>
  <div class="btn btn-red" style="left:91px;top:345px;width:88px;height:36px">Send</div>
</form>

<section class="about"></section>
<div class="big-mark"><span>Summit<br>Coat Works</span></div>
<div class="eyebrow">WELCOME TO <em>SUMMIT COAT WORKS</em></div>
<h2 class="about-title">Lorem <b>Ipsum is simply dummy text of the printing</b> and typesetting.</h2>
<p class="about-copy">There are many variations of passages of Lorem Ipsum available, but the majority have suffered alteration in some form, by injected humour, or randomised words which don't look even slightly believable. If you are going to use a passage of Lorem Ipsum, you need to be sure there isn't anything embarrassing hidden in the middle of text. All the Lorem Ipsum generators on the Internet tend to repeat predefined chunks as necessary, making this the</p>
<div class="btn btn-outline" style="left:613px;top:920px;width:112px;height:37px;font-size:9.5px">Contact Us</div>
<div class="rule"></div>

<h2 class="section-title" style="top:1100px">Our <b>Services</b></h2>

<div class="card">
  <div class="photo" role="img" aria-label="Worker on a lift painting a curved industrial structure" style="left:200px;top:1157px;width:250px;height:156px;background:linear-gradient(135deg,#3d63b0,#7a8aa3)"></div>
  <h3 style="left:200px;top:1330px">Industrial Painting</h3>
  <p style="left:200px;top:1361px">There are many variations of passages of Lorem Ipsum available, but the majority hav suffered alteration ..</p>
  <div class="photo" role="img" aria-label="Stone-fronted commercial retail building" style="left:475px;top:1157px;width:250px;height:156px;background:linear-gradient(180deg,#4a86d6 0%,#9bb6d8 50%,#8b7766 100%)"></div>
  <h3 style="left:475px;top:1330px">Commercial Painting</h3>
  <p style="left:475px;top:1361px">There are many variations of passages of Lorem Ipsum available, but the majority hav suffered alteration ..</p>
  <div class="photo" role="img" aria-label="Crew applying epoxy coating to a warehouse floor" style="left:750px;top:1157px;width:250px;height:156px;background:linear-gradient(180deg,#9a9a9a,#5c5c5c)"></div>
  <h3 style="left:750px;top:1330px">Epoxy Flooring</h3>
  <p style="left:750px;top:1361px">There are many variations of passages of Lorem Ipsum available, but the majority hav suffered alteration ..</p>

  <div class="photo" role="img" aria-label="Bottling line in a food production plant" style="left:200px;top:1434px;width:250px;height:156px;background:linear-gradient(180deg,#b7b1a4,#9a5a1e)"></div>
  <h3 style="left:200px;top:1607px">Food Grade Flooring Systems</h3>
  <p style="left:200px;top:1638px">There are many variations of passages of Lorem Ipsum available, but the majority hav suffered alteration ..</p>
  <div class="photo" role="img" aria-label="Industrial silos and storage tanks" style="left:475px;top:1434px;width:250px;height:156px;background:linear-gradient(180deg,#3f6fc0,#a9b3bf 70%,#6c6f72)"></div>
  <h3 style="left:475px;top:1607px">Silo and Tank Painting</h3>
  <p style="left:475px;top:1638px">There are many variations of passages of Lorem Ipsum available, but the majority hav suffered alteration ..</p>
  <div class="photo" role="img" aria-label="Empty warehouse interior with painting equipment" style="left:750px;top:1434px;width:250px;height:156px;background:linear-gradient(180deg,#c9cdd2,#9ea3a8)"></div>
  <h3 style="left:750px;top:1607px">Warehouse Painting</h3>
  <p style="left:750px;top:1638px">There are many variations of passages of Lorem Ipsum available, but the majority hav suffered alteration ..</p>
</div>
<div class="btn btn-outline" style="left:544px;top:1717px;width:112px;height:37px;font-size:9.5px">View All</div>

<section class="cta">
  <h2>Call for a free, <b>no obligation estimate<br>and expert consultation</b></h2>
  <div class="cta-phone phone-num">
    <svg width="13" height="13" viewBox="0 0 24 24"><path fill="#c20a2e" d="M6.6 10.8a15 15 0 0 0 6.6 6.6l2.2-2.2a1 1 0 0 1 1-.25 11.4 11.4 0 0 0 3.6.57 1 1 0 0 1 1 1V20a1 1 0 0 1-1 1A17 17 0 0 1 3 4a1 1 0 0 1 1-1h3.5a1 1 0 0 1 1 1c0 1.25.2 2.45.57 3.57a1 1 0 0 1-.25 1z"/></svg>123-456-7890</div>
  <svg class="abs" style="left:0;bottom:0" width="1200" height="70" viewBox="0 0 1200 70" preserveAspectRatio="none">
    <path fill="#ffffff" d="M0 66 C100 58 170 70 260 60 C360 48 430 56 520 44 C620 30 700 40 790 32 C880 24 950 30 1040 26 C1110 22 1160 24 1200 22 L1200 70 L0 70Z"/>
  </svg>
</section>

<h2 class="section-title" style="top:2064px">Photo <b>Gallery</b></h2>
<div class="photo" role="img" aria-label="Two-storey commercial office building" style="left:200px;top:2121px;width:250px;height:156px;background:linear-gradient(180deg,#5f95d8,#c8c2b6 60%,#7a8a5a)"></div>
<div class="photo" role="img" aria-label="Grain silos on a farm site" style="left:200px;top:2303px;width:250px;height:156px;background:linear-gradient(180deg,#3f72c6,#b8b9b8 60%,#7a5e3c)"></div>
<div class="photo" role="img" aria-label="Blue industrial warehouse with loading doors" style="left:475px;top:2121px;width:250px;height:338px;background:linear-gradient(180deg,#2e79d8,#2c4f9c 50%,#9aa0a8)"></div>
<div class="photo" role="img" aria-label="Cement plant with silos and crane" style="left:750px;top:2121px;width:250px;height:156px;background:linear-gradient(180deg,#7aa6dc,#c0c4c6 60%,#8d7a5c)"></div>
<div class="photo" role="img" aria-label="Modern white industrial building" style="left:750px;top:2303px;width:250px;height:156px;background:linear-gradient(180deg,#3d7ad3,#d6dbe3 60%,#6d8450)"></div>
<div class="btn btn-outline" style="left:544px;top:2491px;width:112px;height:37px;font-size:9.5px">View All</div>

<footer class="site-footer">
  <div class="foot-brand">Summit<br>Coat Works</div>
  <h4 style="left:431px">Contact Us</h4>
  <div class="contact-line" style="top:98px"><svg width="12" height="12" viewBox="0 0 24 24"><path fill="#c20a2e" d="M6.6 10.8a15 15 0 0 0 6.6 6.6l2.2-2.2a1 1 0 0 1 1-.25 11.4 11.4 0 0 0 3.6.57 1 1 0 0 1 1 1V20a1 1 0 0 1-1 1A17 17 0 0 1 3 4a1 1 0 0 1 1-1h3.5a1 1 0 0 1 1 1c0 1.25.2 2.45.57 3.57a1 1 0 0 1-.25 1z"/></svg><span style="font-size:14px">123-456-7890</span></div>
  <div class="contact-line" style="top:125px"><svg width="12" height="12" viewBox="0 0 24 24"><path fill="#c20a2e" d="M2 5h20v14H2z"/><path fill="none" stroke="#ececec" stroke-width="2" d="M2 5l10 8 10-8"/></svg><span>info@summitcoatworks.com</span></div>
  <div class="contact-line" style="top:150px"><svg width="12" height="14" viewBox="0 0 24 28"><path fill="#c20a2e" d="M12 0a9 9 0 0 0-9 9c0 7 9 19 9 19s9-12 9-19a9 9 0 0 0-9-9zm0 13a4 4 0 1 1 0-8 4 4 0 0 1 0 8z"/></svg><span style="font-size:10px">Summit Coat Works 123<br>Lorem Ipsum, MI-12345</span></div>
  <div class="social" style="left:432px"></div>
  <div class="social" style="left:469px;background:var(--red)"></div>
  <div class="social" style="left:506px"></div>
  <div class="social" style="left:544px"></div>
  <h4 style="left:679px">Our Services</h4>
  <ul class="foot-list" style="left:679px"><li>Industrial Painting</li><li>Commercial Painting</li><li>Epoxy Flooring</li><li>Food Grade Flooring Systems</li><li>Silo and Tank Painting</li><li>Warehouse Painting</li></ul>
  <h4 style="left:881px">Quick Link</h4>
  <ul class="foot-list" style="left:881px"><li>Home</li><li>Services</li><li>Gallery</li><li>Contact Us</li></ul>
  <p class="copyright">© 2023 <em>Summit Coat Works.</em> All Right Reserved</p>
  <svg class="abs" style="left:1041px;top:266px" width="16" height="18" viewBox="0 0 16 18"><path fill="#0c2a6b" d="M8 0L16 18L8 13L0 18Z"/></svg>
</footer>

</body>
</html>
```